Business Cards

Business card design for my company.
I would like the card's background colour to be black. You can also see our web site to get an idea of our brand. https://www.dlqmarrowfield.com.au/
- Name
- Email

```html
<!DOCTYPE html>
<html lang="en">
<head>
<meta charset="utf-8">
<title>DLQ Marrowfield – Business Cards</title>
<link href="https://fonts.googleapis.com/css2?family=Jost:wght@400;500;600;700&display=swap" rel="stylesheet">
<style>
  :root {
    --stage: #2b2b2d;
    --card-black: #0b0b0b;
    --brand-green: #2fae48;
    --brand-green-deep: #17913a;
    --brand-green-light: #45c158;
    --text-white: #f2f2f2;
    --text-dark: #0d2414;
    --dusk-blue: #1d2f52;
    --warm-light: #b7793f;
  }
  * { margin: 0; padding: 0; box-sizing: border-box; }
  html, body { width: 1200px; height: 900px; overflow: hidden; }
  body {
    background: var(--stage);
    font-family: "Jost", "Futura", sans-serif;
    position: relative;
  }
  .card {
    position: absolute;
    width: 620px;
    height: 354px;
    border-radius: 4px;
    overflow: hidden;
    background: var(--card-black);
    box-shadow: 0 14px 30px rgba(0,0,0,0.45);
  }
  .card-front { left: 80px; top: 70px; }
  .card-back { left: 500px; top: 476px; }

  .front-photo {
    position: absolute; inset: 0;
    background:
      radial-gradient(ellipse at 60% 55%, rgba(230,170,100,0.75) 0%, rgba(183,121,63,0.45) 30%, transparent 60%),
      linear-gradient(120deg, var(--dusk-blue) 0%, #2a3550 35%, #5a4a3a 60%, #2c2a2a 100%);
  }
  .card svg.band { position: absolute; inset: 0; }

  .wordmark {
    position: absolute;
    display: flex; align-items: center; gap: 10px;
    color: var(--text-white);
    font-weight: 600;
    letter-spacing: 0.08em;
    text-transform: uppercase;
  }
  .wordmark-dot {
    width: 12px; height: 12px; border-radius: 50%;
    background: var(--brand-green);
  }
  .card-front .wordmark { left: 40px; top: 150px; font-size: 22px; }
  .card-back .wordmark { right: 40px; top: 64px; font-size: 26px; }

  .front-web {
    position: absolute; left: 36px; bottom: 10px;
    color: var(--brand-green);
    font-size: 15px; font-weight: 500; letter-spacing: 0.02em;
  }
  .back-web {
    position: absolute; right: 28px; bottom: 30px;
    color: var(--text-dark);
    font-size: 15px; font-weight: 500;
  }
  .person { position: absolute; left: 40px; top: 178px; }
  .person-name {
    color: var(--brand-green);
    font-size: 22px; font-weight: 700; letter-spacing: 0.03em;
    text-transform: uppercase; line-height: 1.1;
  }
  .person-role { color: var(--text-white); font-size: 15px; margin-top: 2px; }
  .contact-list { list-style: none; margin-top: 16px; }
  .contact-list li {
    display: flex; align-items: center; gap: 9px;
    color: var(--text-white); font-size: 14px; line-height: 1.55;
  }
  .contact-list svg { width: 13px; height: 13px; fill: var(--brand-green); flex: none; }
</style>
</head>
<body>

<section class="card card-front">
  <div class="front-photo" role="img" aria-label="Photograph of a modern two-storey home lit up at dusk, with double garage and timber cladding"></div>
  <svg class="band" viewBox="0 0 620 354" preserveAspectRatio="none" aria-hidden="true">
    <path d="M0 318 L300 318 Q314 318 318 306 Q322 296 336 296 L620 296 L620 354 L0 354 Z" fill="var(--card-black)"/>
  </svg>
  <div class="wordmark"><span class="wordmark-dot"></span>DLQ Marrowfield</div>
  <p class="front-web">www.dlqmarrowfield.com.au</p>
</section>

<section class="card card-back">
  <svg class="band" viewBox="0 0 620 354" preserveAspectRatio="none" aria-hidden="true">
    <defs>
      <linearGradient id="bandGreen" x1="0" y1="0" x2="1" y2="0">
        <stop offset="0" stop-color="var(--brand-green-deep)"/>
        <stop offset="1" stop-color="var(--brand-green-light)"/>
      </linearGradient>
    </defs>
    <path d="M0 334 L372 334 Q386 334 388 320 L391 296 Q393 282 408 282 L620 282 L620 354 L0 354 Z" fill="url(#bandGreen)"/>
  </svg>
  <div class="wordmark"><span class="wordmark-dot"></span>DLQ Marrowfield</div>

  <div class="person">
    <h1 class="person-name">Glen Harlow</h1>
    <p class="person-role">General Manager</p>
    <ul class="contact-list">
      <li><svg viewBox="0 0 24 24"><path d="M6.6 10.8a15 15 0 0 0 6.6 6.6l2.2-2.2a1 1 0 0 1 1-.25 11.4 11.4 0 0 0 3.6.57 1 1 0 0 1 1 1V20a1 1 0 0 1-1 1A17 17 0 0 1 3 4a1 1 0 0 1 1-1h3.5a1 1 0 0 1 1 1c0 1.25.2 2.45.57 3.57a1 1 0 0 1-.25 1z"/></svg>0400 555 182</li>
      <li><svg viewBox="0 0 24 24"><path d="M2 5h20v14H2z M3.5 6.5 12 13l8.5-6.5v-.2h-17z" fill-rule="evenodd"/></svg>info@dlqmarrowfield.com.au</li>
      <li><svg viewBox="0 0 24 24"><path d="M12 2a7 7 0 0 0-7 7c0 5.2 7 13 7 13s7-7.8 7-13a7 7 0 0 0-7-7zm0 9.5A2.5 2.5 0 1 1 12 6.5a2.5 2.5 0 0 1 0 5z"/></svg>Ashvale, Tasmania, Australia</li>
    </ul>
  </div>

  <p class="back-web">www.dlqmarrowfield.com.au</p>
</section>

</body>
</html>
```